Business Card and Word .doc header and footer required

I need a business card designed for my cybersecurity consulting company. Also required, is a header and footer to be ued for my word documents.
Attached is the Logo design, font and rgb used.

Industry/Entity Type

Cyber Security Consulting

Contact Information for Business Card

Name, Phone, email, website

Colors
0054AA
0677BA
7BADD7
CADEEF
E8F1F8

Requirements
Must have
• Sleek, modern

```html
<!DOCTYPE html>
<html lang="en">
<head>
<meta charset="utf-8">
<title>Harrow Vale Consulting – Stationery</title>
<link href="https://fonts.googleapis.com/css2?family=Montserrat:wght@400;500;700&display=swap" rel="stylesheet">
<style>
  :root {
    --navy: #0b1226;
    --ink: #111827;
    --blue-deep: #0054AA;
    --blue: #0677BA;
    --blue-soft: #7BADD7;
    --blue-pale: #CADEEF;
    --blue-mist: #E8F1F8;
    --band: #14204a;
    --backdrop: #e4e6e9;
    --paper: #ffffff;
    --grey: #6b7280;
  }
  * { box-sizing: border-box; margin: 0; padding: 0; }
  html, body { width: 974px; height: 1200px; overflow: hidden; }
  body {
    background: var(--backdrop);
    font-family: "Montserrat", sans-serif;
    position: relative;
  }
  .letterhead {
    position: absolute;
    left: 140px; top: 113px;
    width: 695px; height: 974px;
    background: var(--paper);
  }
  .brand {
    position: absolute;
    display: flex; align-items: center; gap: 10px;
  }
  .brand-dot {
    border-radius: 50%;
    background: var(--blue);
    flex: none;
  }
  .brand-name {
    font-weight: 700;
    color: var(--ink);
    letter-spacing: 0.02em;
    text-transform: uppercase;
    white-space: nowrap;
  }
  .letterhead-brand {
    top: 70px; left: 0; right: 0; justify-content: center;
  }
  .letterhead-brand .brand-dot { width: 22px; height: 22px; }
  .letterhead-brand .brand-name { font-size: 19px; }

  .footer-band {
    position: absolute; left: 0; bottom: 0;
    width: 100%; height: 57px;
    background: linear-gradient(90deg, #13204a, #1a2a5c 50%, #13204a);
    display: flex; align-items: center; justify-content: center;
  }
  .footer-url {
    color: #fff; font-size: 15px; letter-spacing: 0.22em;
  }

  .card {
    position: absolute;
    width: 320px; height: 184px;
    box-shadow: 0 6px 14px rgba(0,0,0,0.25);
    overflow: hidden;
  }
  .card-front {
    left: 100px; top: 330px;
    background: var(--navy);
  }
  .card-front .network {
    position: absolute; left: 0; bottom: 0; width: 100%; height: 80px;
    background: linear-gradient(180deg, rgba(11,18,38,0) 0%, rgba(30,60,130,0.55) 100%);
  }
  .card-front .brand {
    top: 78px; left: 0; right: 0; justify-content: center;
  }
  .card-front .brand-name { color: #e5e7eb; font-size: 19px; }

  .card-back {
    left: 300px; top: 510px;
    background: var(--paper);
  }
  .card-back .brand {
    top: 44px; left: 0; right: 0; justify-content: center;
  }
  .card-back .brand-dot { width: 18px; height: 18px; }
  .card-back .brand-name { font-size: 15px; }
  .contact-row {
    position: absolute; top: 122px; left: 20px; right: 14px;
    display: flex; gap: 10px; align-items: flex-start;
  }
  .person { text-align: right; }
  .person-name { font-weight: 700; font-size: 9.5px; color: var(--ink); }
  .person-role { font-size: 6.5px; color: var(--grey); margin-top: 2px; }
  .details { font-size: 6.5px; color: #374151; }
  .details li { list-style: none; display: flex; align-items: center; gap: 4px; margin-bottom: 4px; }
  .details svg { width: 7px; height: 7px; flex: none; }
</style>
</head>
<body>
  <section class="letterhead">
    <header class="brand letterhead-brand">
      <span class="brand-dot"></span>
      <span class="brand-name">Harrow Vale Consulting</span>
    </header>

    <article class="card card-front">
      <div class="network" role="img" aria-label="Faint blue digital network pattern"></div>
      <div class="brand">
        <span class="brand-name">Harrow Vale Consulting</span>
      </div>
    </article>

    <article class="card card-back">
      <div class="brand">
        <span class="brand-dot"></span>
        <span class="brand-name">Harrow Vale Consulting</span>
      </div>
      <div class="contact-row">
        <div class="person">
          <p class="person-name">DANIEL MARSH</p>
          <p class="person-role">Principal Consultant</p>
        </div>
        <ul class="details">
          <li>
            <svg viewBox="0 0 10 10"><circle cx="5" cy="5" r="5" fill="#0677BA"/><rect x="2.5" y="3.3" width="5" height="3.4" fill="none" stroke="#fff" stroke-width="0.8"/></svg>
            Daniel.Marsh@HarrowValeConsulting.com
          </li>
          <li>
            <svg viewBox="0 0 10 10"><circle cx="5" cy="5" r="5" fill="#0677BA"/><circle cx="5" cy="5" r="2.6" fill="none" stroke="#fff" stroke-width="0.8"/></svg>
            www.HarrowValeConsulting.com
          </li>
        </ul>
      </div>
    </article>

    <footer class="footer-band" role="img" aria-label="Navy band with faint digital network pattern">
      <span class="footer-url">www.HarrowValeConsulting.com</span>
    </footer>
  </section>
</body>
</html>
```